We need a DL size flyer, double sided, for our lawn mowing and gardening business, Kestrel Greens.

We want to run on the front side, the following promotion:
50% off lawn mowing, applies to first lawn mowed on any regular service,
applies to first 100 callers only, so call now!
Professional lawn mowing at an affordable price.

Logo at the bottom left, with Lawn and Garden Maintenance written just below logo.

On bottom Right contact details;
Tom and Gareth
Ph: 0487650912
Email: kestrelgreens@mailbox-example.com
www.kestrelgreens-example.com.au

Front side positioned horizontally, with a bright and colour full design in the background, with the offer of 50% Off lawn mowing in large letters along the top.

On the rear side, also positioned horizontally, a list of our services, stating;

At Kestrel Greens we specialise in the following services;
Lawn mowing
Edging
Blowing
Hedging
Pruning
Tree Loping
Weeding
Poisoning
Mulching
Fertilising
Rubbish removal
Planting
Lawn care and advice
Turf
And any other garden maintenance job,
No job too big or too small.
(No particular order, whatever fits best)
Also include our contact details,
Kestrel Greens
Ph 0487650912
www.kestrelgreens-example.com.au

Target Market(s)

Home owners, aged between 30-50 years old, moderate socio ecenomic status to more afluent areas.

Industry/Entity Type

Business

Requirements
Must have
• DL size, front and back, full colour.
Nice to have
• The writting stating "Kestrel Greens" in our logo is quite bland, if that could also be amended to make it more appealing, but change the writting design only not the actual logo.

```html
<!DOCTYPE html>
<html lang="en">
<head>
<meta charset="utf-8">
<title>Kestrel Greens – DL Flyer, Front and Back</title>
<link href="https://fonts.googleapis.com/css2?family=Roboto+Condensed:wght@400;700&family=PT+Sans:wght@400;700&display=swap" rel="stylesheet">
<style>
  :root{
    --ink:#0b0b0b;
    --leaf:#8cc63f;
    --forest:#1e9a3c;
    --sun:#f5e000;
    --white:#ffffff;
    --silver-hi:#fbfbfb;
    --silver-lo:#cfd2d3;
    --stage:#e9e6e1;
    --head:"Roboto Condensed", Arial Narrow, sans-serif;
    --body:"PT Sans", Arial, sans-serif;
  }
  *{box-sizing:border-box;margin:0;padding:0}
  html,body{width:1200px;height:900px;overflow:hidden;background:var(--stage)}
  .sheet{position:relative;width:1200px;height:900px}
  .flyer{position:absolute;left:170px;width:860px;height:406px;overflow:hidden;background:var(--ink);box-shadow:0 6px 18px rgba(0,0,0,.25)}
  .flyer--front{top:29px}
  .flyer--back{top:465px}
  .flyer__art{position:absolute;inset:0;width:860px;height:406px}

  /* front */
  .offer{position:absolute;left:24px;top:44px;transform:rotate(-6deg);transform-origin:left top}
  .offer__head{display:flex;align-items:center;gap:12px}
  .offer__badge{width:64px;height:64px;border-radius:50%;background:var(--white);display:flex;align-items:center;justify-content:center;flex:none}
  .offer__badge span{width:56px;height:56px;border-radius:50%;background:var(--forest);color:var(--white);font:700 20px/56px var(--head);text-align:center}
  .offer__title{color:var(--sun);font:700 28px/1 var(--head);white-space:nowrap}
  .offer__terms{margin-top:8px;padding-left:6px;white-space:nowrap;color:var(--leaf);font:700 21px/26px var(--head)}
  .offer__terms .lead{color:var(--white)}
  .tagline{position:absolute;left:200px;top:330px;color:var(--sun);font:700 21px/1 var(--head);white-space:nowrap}
  .contact-strip{position:absolute;left:0;right:0;bottom:0;height:38px;background:var(--leaf);display:flex;align-items:center;gap:18px;padding-left:22px;color:var(--ink);font:700 14px/1 var(--body)}
  .contact-strip .item{display:flex;align-items:center;gap:6px}
  .icon{width:14px;height:14px;flex:none}
  .brand{display:flex;align-items:center;gap:8px}
  .brand__dot{width:16px;height:16px;border-radius:50%;background:var(--sun);flex:none}
  .brand__name{font:700 22px/1 var(--head);color:var(--white);white-space:nowrap}
  .front-brand{position:absolute;right:0;top:200px;width:172px;height:118px;background:var(--leaf);padding:24px 14px 0}
  .front-brand .brand__name{font-size:21px}
  .front-brand__sub{margin-top:14px;color:var(--ink);font:700 13px/1.2 var(--head);text-transform:uppercase;letter-spacing:.5px}

  /* back */
  .back-brand{position:absolute;left:34px;top:190px}
  .back-brand__sub{margin-top:12px;color:var(--leaf);font:700 19px/1.15 var(--head);width:150px}
  .services{position:absolute;left:250px;top:62px}
  .services__heading{color:var(--leaf);font:700 19px/1 var(--head);white-space:nowrap}
  .services__cols{display:flex;gap:30px;margin-top:18px}
  .services__list{list-style:none}
  .services__list li{position:relative;padding-left:18px;color:var(--white);font:400 15px/22px var(--body);white-space:nowrap}
  .services__list li::before{content:"";position:absolute;left:2px;top:8px;width:7px;height:7px;background:var(--sun);transform:rotate(45deg)}
  .services__list .wrap{white-space:normal;width:150px}
  .back-contact{position:absolute;right:26px;top:322px;text-align:right;color:var(--forest);font:700 15px/21px var(--body)}
  .back-contact .row{display:flex;justify-content:flex-end;align-items:center;gap:8px}
  .back-contact .names{margin-right:8px}
</style>
</head>
<body>
<main class="sheet">

  <!-- FRONT SIDE -->
  <section class="flyer flyer--front" aria-label="Flyer front">
    <svg class="flyer__art" viewBox="0 0 860 406">
      <defs>
        <linearGradient id="garden-tones" x1="0" y1="1" x2="1" y2="0">
          <stop offset="0" stop-color="#3f6b2a"/>
          <stop offset=".5" stop-color="#6f8f4a"/>
          <stop offset="1" stop-color="#8a8576"/>
        </linearGradient>
      </defs>
      <path role="img" aria-label="Photo collage of mowed lawns, garden beds, stone wall, mower and blower"
            d="M0,318 L0,292 C420,282 640,200 720,0 L860,0 L860,318 Z" fill="url(#garden-tones)"/>
      <g fill="none">
        <path d="M0,292 C420,282 640,200 720,0" stroke="var(--leaf)" stroke-width="10" transform="translate(-2,-5)"/>
        <path d="M0,292 C420,282 640,200 720,0" stroke="var(--forest)" stroke-width="9" transform="translate(-6,-15)"/>
        <path d="M0,292 C420,282 640,200 720,0" stroke="var(--sun)" stroke-width="7" transform="translate(-10,-24)"/>
      </g>
      <rect x="0" y="318" width="860" height="50" fill="var(--ink)"/>
    </svg>

    <div class="offer">
      <div class="offer__head">
        <div class="offer__badge"><span>50%</span></div>
        <p class="offer__title">Off Lawn Mowing</p>
      </div>
      <p class="offer__terms"><span class="lead">Applies to first lawn mowed on any regular Service,</span><br>Applies to first 100 Callers Only, So call now !</p>
    </div>

    <div class="front-brand">
      <div class="brand"><span class="brand__dot"></span><span class="brand__name">Kestrel Greens</span></div>
      <p class="front-brand__sub">Lawn &amp; Garden<br>Maintenance</p>
    </div>

    <p class="tagline">Proffesional lawn Mowing at an affordable Price !</p>

    <div class="contact-strip">
      <span class="item">Tom and Gareth</span>
      <span class="item">
        <svg class="icon" viewBox="0 0 16 16"><path d="M4 1l3 3-2 2c1 2 3 4 5 5l2-2 3 3-2 2C7 14 2 9 2 3z" fill="currentColor"/></svg>
        0487650912</span>
      <span class="item">
        <svg class="icon" viewBox="0 0 16 16"><rect x="1" y="3" width="14" height="10" fill="currentColor"/><path d="M1 3l7 6 7-6" fill="none" stroke="var(--leaf)" stroke-width="1.5"/></svg>
        kestrelgreens@mailbox-example.com</span>
      <span class="item">
        <svg class="icon" viewBox="0 0 16 16"><circle cx="8" cy="8" r="6.5" fill="none" stroke="currentColor" stroke-width="1.6"/><path d="M1.5 8h13M8 1.5c-3 3.5-3 9.5 0 13M8 1.5c3 3.5 3 9.5 0 13" fill="none" stroke="currentColor" stroke-width="1.2"/></svg>
        www.kestrelgreens-example.com.au</span>
    </div>
  </section>

  <!-- BACK SIDE -->
  <section class="flyer flyer--back" aria-label="Flyer back">
    <svg class="flyer__art" viewBox="0 0 860 406" aria-hidden="true">
      <defs>
        <linearGradient id="silver" x1="0" y1="0" x2="1" y2="1">
          <stop offset="0" stop-color="var(--silver-hi)"/>
          <stop offset="1" stop-color="var(--silver-lo)"/>
        </linearGradient>
      </defs>
      <path d="M380,406 C540,330 740,250 860,150 L860,406 Z" fill="url(#silver)"/>
      <path d="M380,406 C540,330 740,250 860,150" fill="none" stroke="var(--sun)" stroke-width="10" transform="translate(-6,-4)"/>
      <path d="M380,406 C540,330 740,250 860,150" fill="none" stroke="var(--forest)" stroke-width="11" transform="translate(-14,-14)"/>
      <path d="M380,406 C540,330 740,250 860,150" fill="none" stroke="var(--leaf)" stroke-width="12" transform="translate(-24,-26)"/>
    </svg>

    <div class="back-brand">
      <div class="brand"><span class="brand__dot"></span><span class="brand__name">Kestrel Greens</span></div>
      <p class="back-brand__sub">Lawn and Garden Maintenance</p>
    </div>

    <div class="services">
      <p class="services__heading">At Kestrel Greens we specialise in the following services;</p>
      <div class="services__cols">
        <ul class="services__list">
          <li>Lawn mowing</li><li>Edging</li><li>Blowing</li><li>Hedging</li><li>Pruning</li>
        </ul>
        <ul class="services__list">
          <li>Tree Loping</li><li>Weeding</li><li>Poisoning</li><li>Mulching</li><li>Fertilising</li>
        </ul>
        <ul class="services__list">
          <li>Rubbish removal</li><li>Planting</li><li>Lawn care and advice</li><li>Turf</li><li class="wrap">And any other garden maintenance job !</li>
        </ul>
      </div>
    </div>

    <div class="back-contact">
      <div class="row"><span class="names">Tom and Gareth</span>
        <svg class="icon" viewBox="0 0 16 16"><path d="M4 1l3 3-2 2c1 2 3 4 5 5l2-2 3 3-2 2C7 14 2 9 2 3z" fill="currentColor"/></svg>
        <span>0487650912</span></div>
      <div class="row">
        <svg class="icon" viewBox="0 0 16 16"><rect x="1" y="3" width="14" height="10" fill="currentColor"/><path d="M1 3l7 6 7-6" fill="none" stroke="var(--white)" stroke-width="1.5"/></svg>
        <span>kestrelgreens@mailbox-example.com</span></div>
      <div class="row"><span>www.kestrelgreens-example.com.au</span></div>
    </div>
  </section>

</main>
</body>
</html>
```